I need a business card design for a new company that will be doing consulting work around issues of cultural competency, and diversity and inclusion. I would like the design to be crisp and clear with bold but conservative colors and incorporate shades of blue

Target Market(s)

Small businesses, schools, non-profits

Industry/Entity Type

Consulting

Font styles to use
Serif
Sans Serif

Colors
0c5ba6
6b449b
3276b5
0292cd

Requirements
Must have
• A Morrow Venture (name of company)
• Lemlem Tavish
• CEO
• lemlem@amorrowventure.com
• (215)483-2756

```html
<!DOCTYPE html>
<html lang="en">
<head>
<meta charset="utf-8">
<title>A Morrow Venture — Business Card</title>
<link rel="stylesheet" href="https://fonts.googleapis.com/css2?family=Quicksand:wght@400;500;700&display=swap">
<style>
  :root {
    --page-bg: #e9ebee;
    --card-bg: #f4f5f7;
    --brand-blue: #3f7bb8;
    --brand-blue-deep: #3276b5;
    --ring-blue: #4d9bd9;
    --charcoal: #2e3034;
    --ink: #2b2d31;
    --white: #ffffff;
  }
  * { margin: 0; padding: 0; box-sizing: border-box; }
  html, body {
    width: 1200px; height: 789px; overflow: hidden;
    background: var(--page-bg);
  }
  .card {
    position: absolute; left: 75px; top: 95px;
    width: 1050px; height: 600px;
    background: var(--card-bg);
    border-radius: 4px;
    box-shadow: 0 10px 30px rgba(0,0,0,0.18);
    overflow: hidden;
  }
  .card-shapes { position: absolute; inset: 0; }
  .company-name {
    position: absolute; left: 70px; top: 205px;
    width: 420px;
    font-family: "Quicksand", sans-serif; font-weight: 500;
    font-size: 44px; line-height: 1.1;
    color: var(--brand-blue-deep);
    text-align: center;
    white-space: nowrap;
  }
  .person {
    position: absolute; right: 60px; top: 100px;
    text-align: right; color: var(--white);
    font-family: "Quicksand", sans-serif;
  }
  .person-name { font-size: 58px; line-height: 1; }
  .person-name .first { font-weight: 700; }
  .person-name .last { font-weight: 400; }
  .person-title {
    font-size: 34px; font-weight: 400; letter-spacing: 2px;
    margin-top: 2px; margin-right: 110px;
  }
  .contact {
    position: absolute; left: 660px;
    font-family: "Quicksand", sans-serif; font-weight: 500;
    font-size: 25px; line-height: 1.25; color: var(--ink);
  }
  .contact-phone { top: 315px; }
  .contact-web { top: 380px; }
  .contact-address { top: 455px; }
</style>
</head>
<body>
  <div class="card">
    <svg class="card-shapes" width="1050" height="600" viewBox="0 0 1050 600" aria-hidden="true">
      <path d="M545 95 Q530 95 536 109 L582 220 Q588 235 604 235 L1050 235 L1050 95 Z" fill="var(--brand-blue)"/>
      <path d="M0 420 L520 420 Q534 420 538 434 L578 600 L0 600 Z" fill="var(--brand-blue)"/>
      <path d="M590 560 Q575 560 578 575 L584 600 L1050 600 L1050 560 Z" fill="var(--charcoal)"/>
      <line x1="615" y1="330" x2="615" y2="470" stroke="var(--ring-blue)" stroke-width="6"/>
      <g class="contact-icon phone">
        <circle cx="615" cy="330" r="24" fill="var(--card-bg)" stroke="var(--ring-blue)" stroke-width="5"/>
        <circle cx="615" cy="330" r="16" fill="var(--charcoal)"/>
        <path d="M609 321 l4 0 l1 5 l-2 2 q2 4 6 6 l2 -2 l5 1 l0 4 q-1 2 -3 2 q-9 -1 -14 -9 q-2 -4 -1 -7 q0 -2 2 -2 z" fill="var(--white)"/>
      </g>
      <g class="contact-icon globe">
        <circle cx="615" cy="400" r="24" fill="var(--card-bg)" stroke="var(--ring-blue)" stroke-width="5"/>
        <circle cx="615" cy="400" r="16" fill="var(--charcoal)"/>
        <circle cx="615" cy="400" r="9" fill="none" stroke="var(--white)" stroke-width="2"/>
        <line x1="606" y1="400" x2="624" y2="400" stroke="var(--white)" stroke-width="2"/>
        <ellipse cx="615" cy="400" rx="4" ry="9" fill="none" stroke="var(--white)" stroke-width="2"/>
      </g>
      <g class="contact-icon pin">
        <circle cx="615" cy="470" r="24" fill="var(--card-bg)" stroke="var(--ring-blue)" stroke-width="5"/>
        <circle cx="615" cy="470" r="16" fill="var(--charcoal)"/>
        <path d="M615 480 q-7 -8 -7 -13 a7 7 0 0 1 14 0 q0 5 -7 13 z" fill="var(--white)"/>
        <circle cx="615" cy="467" r="2.5" fill="var(--charcoal)"/>
      </g>
    </svg>

    <div class="company-name">A Morrow Venture</div>

    <div class="person">
      <div class="person-name"><span class="first">Lemlem</span> <span class="last">Tavish</span></div>
      <div class="person-title">CEO</div>
    </div>

    <div class="contact contact-phone">(215)483-2756</div>
    <div class="contact contact-web">lemlem@amorrowventure.com<br>www.amorrowventure.com</div>
    <div class="contact contact-address">48, Alder Lane, Your<br>City, New York, USA 102938</div>
  </div>
</body>
</html>
```